Wildlife photographer Website

The website is to be a "resume" of pictures and awards won by Nora. Lean heavy to outdoor wildlife.
She will post articles and have ability to interact with fans.

I will add some of her pictures tonight,

Target Market(s)

Terra Quarterly .....anyone looking to hire a wildlife photographer.

Industry/Entity Type

Professional Photography

Contact Information for Business Card

Nora Falkett
4817 Maple Hollow Lane
Columbia MD 21078
443-581-2094
Nora@FernOwlPix.com

Coding

Coded - Design and coding required

Number of Pages Required

5+ page

Requirements
Must have
• New Logo
Nice to have
• Nature, and eye catching graphics

```html
<!DOCTYPE html>
<html lang="en">
<head>
<meta charset="utf-8">
<title>Wildlife Photographer</title>
<link href="https://fonts.googleapis.com/css2?family=Roboto:wght@400;500;700&family=Lato:wght@400;700&family=Poppins:wght@400;600&display=swap" rel="stylesheet">
<style>
:root{
  --green:#5c9260;
  --ink:#333333;
  --muted:#666666;
  --black:#0b0b0b;
  --footer:#1c1c1c;
  --footer-deep:#121212;
  --card:#555555;
  --light:#efefef;
  --white:#ffffff;
}
*{margin:0;padding:0;box-sizing:border-box}
html,body{width:1200px;height:2977px;overflow:hidden}
body{position:relative;font-family:"Lato",sans-serif;color:var(--ink);background:var(--white)}
.abs{position:absolute}
.topbar{left:0;top:0;width:1200px;height:53px;background:var(--black);border-bottom:1px solid #2a2a2a}
.brand{left:148px;top:10px;font:700 27px "Roboto",sans-serif;color:var(--white)}
.top-phone{left:820px;top:18px;color:var(--white);font:500 14px "Roboto",sans-serif;display:flex;gap:8px;align-items:center}
.top-mail{left:975px;top:18px}
.nav{left:0;top:53px;width:1200px;height:49px;background:rgba(10,10,10,.92);border-bottom:1px solid #333}
.nav a{position:absolute;top:17px;font:500 14px "Roboto",sans-serif;color:var(--white);text-decoration:none;transform:translateX(-50%)}
.nav .sep{position:absolute;top:16px;width:1px;height:18px;background:#555}
.hero{left:0;top:0;width:1200px;height:715px;overflow:hidden}
.hero-photo{position:absolute;inset:0;background:radial-gradient(ellipse at 70% 45%,#a9774a 0%,#7a5a40 22%,#2e3e66 50%,#1f2a48 80%,#16203a 100%)}
.hero-shade{position:absolute;inset:0;background:linear-gradient(90deg,rgba(0,0,0,.35),rgba(0,0,0,0) 60%)}
.hero-kicker{left:225px;top:245px;font:400 18px "Lato",sans-serif;color:var(--white)}
.hero-title{left:225px;top:278px;font:700 46px "Roboto",sans-serif;color:var(--white);letter-spacing:-.5px}
.hero-text{left:225px;top:342px;width:540px;font:400 18px/27px "Lato",sans-serif;color:var(--white)}
.hero-btn{left:228px;top:431px;width:159px;height:44px;border-radius:22px;background:var(--green);color:var(--white);font:500 16px "Roboto",sans-serif;display:flex;align-items:center;justify-content:center}
.hero-arrow{top:314px;width:40px;height:40px;border:2px solid var(--white);border-radius:50%}
.dot{top:575px;width:13px;height:13px;border:2px solid var(--white);border-radius:50%}
.dot.on{background:var(--white)}
.photo{background:#888}
.eyebrow{left:687px;top:824px;font:400 14px "Lato",sans-serif;color:#222}
.about-title{left:687px;top:852px;width:380px;font:500 29px/37px "Roboto",sans-serif;color:#222}
.about-text{left:687px;top:936px;width:355px;font:400 13.5px/23px "Lato",sans-serif;color:var(--muted)}
.btn-sm{left:687px;top:1099px;width:109px;height:37px;background:var(--green);color:var(--white);font:400 14px "Lato",sans-serif;display:flex;align-items:center;justify-content:center;border-radius:2px}
.section-title{left:0;width:1200px;text-align:center;font:500 35px "Roboto",sans-serif;color:#444}
.section-title span{color:var(--green)}
.underline{left:577px;top:1865px;width:46px;height:2px;background:var(--green)}
.quote{top:1893px;width:278px;height:128px;background:var(--card);color:var(--white);padding:22px 19px}
.quote h4{font:700 14px "Lato",sans-serif;margin-bottom:9px}
.quote p{font:400 11.5px/18px "Lato",sans-serif;color:#e8e8e8}
.quote::after{content:"";position:absolute;left:14px;bottom:-14px;border-left:16px solid var(--card);border-bottom:14px solid transparent}
.avatar{top:2048px;width:45px;height:45px;background:linear-gradient(#c8b8a8,#8a7a6e)}
.who{top:2054px}
.who b{display:block;font:400 14px "Lato",sans-serif;color:#333}
.who i{display:block;font-style:normal;font:400 11.5px "Lato",sans-serif;color:#777;margin-top:3px}
.touch{left:0;top:2183px;width:1200px;height:457px;background:var(--light)}
.touch-title{left:0;top:2249px;width:1200px;text-align:center;font:600 28px "Poppins",sans-serif;color:#222}
.field{background:var(--white);border-radius:4px;font:400 14px "Poppins",sans-serif;color:#888;padding:13px 20px;box-shadow:0 2px 8px rgba(0,0,0,.04)}
.submit{left:528px;top:2548px;width:142px;height:44px;background:var(--green);color:var(--white);font:600 14px "Poppins",sans-serif;display:flex;align-items:center;justify-content:center;border-radius:2px}
.footer{left:0;top:2640px;width:1200px;height:294px;background:var(--footer)}
.fhead{font:700 14px "Lato",sans-serif;color:var(--white)}
.ficon{width:38px;height:38px;border-radius:50%;background:#262626;display:flex;align-items:center;justify-content:center}
.ftext{color:#cfcfcf;font:400 14px "Lato",sans-serif}
.services li{list-style:none;font:400 11.5px "Lato",sans-serif;color:#bbb;height:28px;display:flex;align-items:center;gap:9px}
.services li::before{content:"›";color:var(--green);font-size:15px}
.sub-field{left:740px;top:2730px;width:307px;height:37px;border-radius:19px;background:var(--white);overflow:hidden;display:flex}
.sub-field span{flex:1;padding:10px 22px;font:400 13px "Lato",sans-serif;color:#777}
.sub-field b{width:104px;background:var(--green);color:var(--white);font:400 15px "Lato",sans-serif;display:flex;align-items:center;justify-content:center}
.social{top:2835px;width:38px;height:38px;border-radius:50%;background:var(--green)}
.copy{left:0;top:2934px;width:1200px;height:43px;background:var(--footer-deep);color:#888;font:400 11.5px "Lato",sans-serif;display:flex;align-items:center;justify-content:center}
</style>
</head>
<body>

<section class="hero abs">
  <div class="hero-photo" role="img" aria-label="Photo of a brown hare leaping across snow"></div>
  <div class="hero-shade"></div>
  <svg class="abs" style="left:0;top:600px" width="1200" height="115" viewBox="0 0 1200 115">
    <path d="M0 18 Q600 190 1200 18 L1200 115 L0 115 Z" fill="var(--green)"/>
    <path d="M0 22 Q600 178 1200 22 L1200 115 L0 115 Z" fill="var(--white)"/>
  </svg>
  <p class="abs hero-kicker">Photographer</p>
  <h1 class="abs hero-title">Wildlife Photographer</h1>
  <p class="abs hero-text">Lorem Ipsum is simply dummy text of the printing and typesetting industry. Lorem Ipsum has been the industry's</p>
  <div class="abs hero-btn">LEARN MORE</div>
  <div class="abs hero-arrow" style="left:126px">
    <svg width="36" height="36" viewBox="0 0 36 36"><path d="M20 12 L14 18 L20 24" stroke="#fff" stroke-width="2" fill="none"/></svg>
  </div>
  <div class="abs hero-arrow" style="left:1033px">
    <svg width="36" height="36" viewBox="0 0 36 36"><path d="M16 12 L22 18 L16 24" stroke="#fff" stroke-width="2" fill="none"/></svg>
  </div>
  <span class="abs dot" style="left:578px"></span>
  <span class="abs dot on" style="left:601px"></span>
  <span class="abs dot" style="left:624px"></span>
  <span class="abs dot" style="left:647px"></span>
</section>

<header class="abs topbar">
  <div class="abs brand">Wildlife Photographer</div>
  <div class="abs top-phone">
    <svg width="18" height="18" viewBox="0 0 24 24"><path d="M6 3 L9 3 L10.5 7.5 L8.5 9 Q10 13 15 15.5 L16.5 13.5 L21 15 L21 18 Q21 21 18 21 Q4 20 3 6 Q3 3 6 3 Z" fill="none" stroke="#fff" stroke-width="1.6"/></svg>
    443-581-2094
  </div>
  <svg class="abs top-mail" width="22" height="16" viewBox="0 0 22 16"><rect x="1" y="1" width="20" height="14" fill="none" stroke="#fff" stroke-width="1.5"/><path d="M1 1 L11 9 L21 1 M1 15 L8 7 M21 15 L14 7" fill="none" stroke="#fff" stroke-width="1.5"/></svg>
</header>

<nav class="abs nav">
  <a style="left:364px">HOME</a>
  <span class="sep" style="left:417px"></span>
  <a style="left:468px">ABOUT</a>
  <span class="sep" style="left:518px"></span>
  <a style="left:590px">SERVICES &#9662;</a>
  <span class="sep" style="left:644px"></span>
  <a style="left:702px">GALLERY</a>
  <span class="sep" style="left:759px"></span>
  <a style="left:824px">CONTACT</a>
</nav>

<div class="abs photo" style="left:150px;top:803px;width:256px;height:168px;background:linear-gradient(135deg,#6e7f8f,#3e4c5a 60%,#7b7060)" role="img" aria-label="Photo of a blue heron in flight over water"></div>
<div class="abs photo" style="left:258px;top:988px;width:148px;height:169px;background:linear-gradient(#7d8a96,#b8a282 55%,#9a8162)" role="img" aria-label="Photo of a sandpiper on the beach"></div>
<div class="abs photo" style="left:425px;top:822px;width:198px;height:318px;background:linear-gradient(#8a8e94,#7a7e84)" role="img" aria-label="Photo of two snow geese flying"></div>

<p class="abs eyebrow">WELCOME TO WILDLIFE PHOTOGRAPHER</p>
<h2 class="abs about-title">Lorem Ipsum is simply dummy text of the</h2>
<p class="abs about-text">Lorem Ipsum is simply dummy text of the printing and typesetting industry. Lorem Ipsum has been the industry's standard dummy text ever since the 1500s, when an unknown printer took a galley of type and scrambled it to make a type specimen book. It has survived not only five centuries, but also the leap into electronic typesetting, remaining essentially.</p>
<div class="abs btn-sm">Learn More</div>

<h2 class="abs section-title" style="top:1236px">Latest <span>Photos</span></h2>
<div class="abs photo" style="left:161px;top:1318px;width:435px;height:434px;background:linear-gradient(#3c5678,#1f3552)" role="img" aria-label="Photo of harlequin ducks swimming"></div>
<div class="abs photo" style="left:603px;top:1318px;width:435px;height:214px;background:linear-gradient(#5a7488,#3a5466)" role="img" aria-label="Photo of a long-tailed duck on water"></div>
<div class="abs photo" style="left:603px;top:1539px;width:214px;height:213px;background:linear-gradient(#4a5234,#7a5a36)" role="img" aria-label="Photo of a red fox in the grass"></div>
<div class="abs photo" style="left:824px;top:1539px;width:214px;height:213px;background:linear-gradient(#a9b3aa,#7e8a7c)" role="img" aria-label="Photo of a duck spreading its wings"></div>

<h2 class="abs section-title" style="top:1817px">Our <span>Client Say</span></h2>
<div class="abs underline"></div>

<div class="abs quote" style="left:161px"><h4>“Quality Design”</h4><p>Donec fringilla nunc vitae facilisis ornar a lacinia non nibh. Maecenas sit amet arcu eget leo pellentesque euismod.</p></div>
<div class="abs quote" style="left:461px"><h4>“Super Support”</h4><p>Cras id maximus neque, ullamcorper se orn amet, lacinia non nibh. Maecenas sit amet arcu eget leo pellentesque the compen.</p></div>
<div class="abs quote" style="left:761px"><h4>“Quality Design”</h4><p>Orci varius natoque ullamcorper sed or amet, lacinia non nibh. Maecenas sit amet arcu eget leo pellentesque the euismod.</p></div>

<div class="abs avatar" style="left:161px" role="img" aria-label="Client portrait"></div>
<div class="abs who" style="left:217px"><b>Marcus Delveny</b><i>Designer in Brightleaf</i></div>
<div class="abs avatar" style="left:461px" role="img" aria-label="Client portrait"></div>
<div class="abs who" style="left:517px"><b>Ivy Tremont</b><i>Marketing in Brightleaf</i></div>
<div class="abs avatar" style="left:761px" role="img" aria-label="Client portrait"></div>
<div class="abs who" style="left:817px"><b>Owen Castellar</b><i>Developers in Brightleaf</i></div>

<section class="abs touch"></section>
<h2 class="abs touch-title">Get In Touch</h2>
<div class="abs field" style="left:310px;top:2313px;width:278px;height:44px">Full name</div>
<div class="abs field" style="left:612px;top:2313px;width:278px;height:44px">Email</div>
<div class="abs field" style="left:311px;top:2386px;width:577px;height:126px">Message</div>
<div class="abs submit">SUBMIT</div>

<footer class="abs footer"></footer>
<p class="abs fhead" style="left:220px;top:2690px">CONTACT US</p>
<div class="abs ficon" style="left:219px;top:2739px">
  <svg width="14" height="16" viewBox="0 0 14 16"><rect x="3" y="1" width="8" height="14" rx="1.5" fill="none" stroke="var(--green)" stroke-width="1.5"/><circle cx="7" cy="12.5" r=".9" fill="var(--green)"/></svg>
</div>
<p class="abs ftext" style="left:268px;top:2747px;font-size:17px">443-581-2094</p>
<div class="abs ficon" style="left:219px;top:2800px">
  <svg width="14" height="16" viewBox="0 0 14 16"><path d="M7 15 Q1 8 1 6 A6 6 0 0 1 13 6 Q13 8 7 15 Z" fill="var(--green)"/><circle cx="7" cy="6" r="2" fill="#262626"/></svg>
</div>
<p class="abs ftext" style="left:268px;top:2793px">Nora Falkett</p>
<p class="abs ftext" style="left:268px;top:2811px">4817 Maple Hollow Lane</p>
<p class="abs ftext" style="left:268px;top:2831px;font-size:11.5px;color:#999">Columbia MD 21078</p>
<div class="abs ficon" style="left:219px;top:2850px">
  <svg width="15" height="12" viewBox="0 0 15 12"><rect x="1" y="1" width="13" height="10" fill="none" stroke="var(--green)" stroke-width="1.4"/><path d="M1 1 L7.5 6.5 L14 1" fill="none" stroke="var(--green)" stroke-width="1.4"/></svg>
</div>
<p class="abs ftext" style="left:268px;top:2862px;font-size:11.5px">Nora@FernOwlPix.com</p>

<p class="abs fhead" style="left:541px;top:2690px">OUR SERVICES</p>
<ul class="abs services" style="left:541px;top:2722px">
  <li>Home</li><li>About Us</li><li>Services</li><li>Gallery</li><li>Sitemap</li><li>Contact Us</li>
</ul>

<p class="abs fhead" style="left:747px;top:2689px;font-size:13px">SUBSCRIBE</p>
<div class="abs sub-field"><span>Email address</span><b>Subscribe</b></div>
<p class="abs fhead" style="left:747px;top:2800px;font-size:13px">FOLLOW US</p>
<span class="abs social" style="left:747px" role="img" aria-label="Social link"></span>
<span class="abs social" style="left:790px" role="img" aria-label="Social link"></span>
<span class="abs social" style="left:833px" role="img" aria-label="Social link"></span>
<span class="abs social" style="left:879px" role="img" aria-label="Social link"></span>

<div class="abs copy">Copyright © 2021 Wildlife photographer</div>

</body>
</html>
```